Anzeigengestaltung für ein Hörakustikunternehmen
Zielgruppe
Wir sind ein lokales Hörakustikunternehmen aus Krefeld und zählen zu den ältesten Akustikern in Deutschland.
Unsere Kundengruppe ist m&w ab einem Alter von 50 Jahren, (Silversurfer!) mit einer guten Kaufkraft und in der Freizeit gerne aktiv.
Unsere tägliche Arbeit ist die Hörberatung & Anpassung von Hörsystemen sowie die Beratung und Anpassung von Gehörschutz
Bei dem Design soll auffallen, dass die leisen Töne des Lebens fehlen, wir z.B. das Vogelgetzwitscher oder andere Naturgeräusche. Die Anzeige soll in einer Jagdzeitschrift erscheinen und auch in anderen Medien einsetzbar sien
Aufgabenstellung
Es soll individuell sein und zu unserem Gesamtauftritt passen, siehe Internetseite!
Die Maße können DIN A5 oder die Hälfte davon sein.
Fotos müssen nicht von uns verwendet werden,

```html
<!DOCTYPE html>
<html lang="de">
<head>
<meta charset="utf-8">
<title>Velmaris – Anzeige</title>
<link href="https://fonts.googleapis.com/css2?family=Source+Sans+3:wght@300;400;600;700&display=swap" rel="stylesheet">
<style>
  :root {
    --paper: #ffffff;
    --frame: #9a9a9a;
    --brand-red: #d9442b;
    --brand-grey: #6f6f6f;
    --band: #8c8c8c;
    --text-grey: #7a7a7a;
    --text-dark: #666666;
    --white: #ffffff;
  }
  * { margin: 0; padding: 0; box-sizing: border-box; }
  html, body { width: 846px; height: 1200px; overflow: hidden; background: var(--paper); }
  body { font-family: "Source Sans 3", Arial, sans-serif; }
  .ad {
    position: relative; width: 846px; height: 1200px;
    background: var(--paper); border: 2px solid var(--frame); overflow: hidden;
  }
  .brand {
    position: absolute; left: 66px; top: 62px;
    display: flex; align-items: center; gap: 14px;
  }
  .brand-square { width: 22px; height: 22px; background: var(--brand-red); }
  .brand-name {
    font-size: 46px; font-weight: 400; letter-spacing: 3px;
    color: var(--brand-grey); line-height: 1;
  }
  .hero {
    position: absolute; left: 0; top: 179px; width: 100%; height: 647px;
    background:
      radial-gradient(ellipse at 20% 25%, #b9d77a 0%, rgba(185,215,122,0) 45%),
      radial-gradient(ellipse at 75% 55%, #c9b58e 0%, rgba(201,181,142,0) 40%),
      radial-gradient(ellipse at 50% 40%, #7d7d86 0%, rgba(125,125,134,0) 35%),
      linear-gradient(180deg, #5f8a35 0%, #48702a 45%, #3d5a2a 75%, #4a4a3a 100%);
  }
  .headline {
    position: absolute; left: 64px; top: 428px;
    color: var(--white); line-height: 76px; font-size: 78px;
  }
  .headline-strong { display: block; font-weight: 700; letter-spacing: -0.5px; }
  .headline-light { display: block; font-weight: 300; }
  .intro {
    position: absolute; left: 0; top: 826px; width: 100%; height: 169px;
    background: var(--band); padding: 26px 40px 0 64px;
    color: var(--white); font-size: 16.2px; font-weight: 600; line-height: 29px;
    white-space: nowrap;
  }
  .contact { position: absolute; left: 64px; top: 1024px; color: var(--text-grey); font-size: 15.5px; line-height: 29px; }
  .contact-company { font-weight: 600; color: var(--text-dark); }
  .web { position: absolute; left: 64px; top: 1140px; color: var(--text-grey); font-size: 15.5px; }
</style>
</head>
<body>
  <div class="ad">
    <div class="brand">
      <span class="brand-square"></span>
      <span class="brand-name">VELMARIS</span>
    </div>

    <div class="hero" role="img" aria-label="Foto: ein Paar mittleren Alters spaziert lächelnd durch einen sonnigen Laubwald"></div>

    <h1 class="headline">
      <span class="headline-strong">Aktiv leben.</span>
      <span class="headline-light">Und den Wald</span>
      <span class="headline-light">wieder mit allen</span>
      <span class="headline-light">Sinnen erleben.</span>
    </h1>

    <p class="intro">
      Unsere Kompetenz für Hörsysteme und deren individuelle Anpassung macht uns zum heraus-<br>
      ragenden Hörberater, der dem Kunden das Gesamtsystem „Hörgerät“ aus einer Hand anbieten<br>
      kann. Im Mittelpunkt unserer Aktivitäten stehen die Optimierung des Sprachverstehens und die<br>
      Steigerung des Tragekomforts für unsere Kunden. Lernen Sie uns kennen!
    </p>

    <div class="contact">
      <p class="contact-company">Brunnenfeld GmbH, Lindenallee 12, 31245 Halvenstedt</p>
      <p>Unsere regulären Öffnungszeiten sind Montag bis Freitag von 09:00 bis 13:00 Uhr und von 14:00 bis 18:00 Uhr.</p>
      <p>Individuelle Terminvereinbarung unter: 04721 - 40 61 7</p>
    </div>

    <p class="web">www.velmaris-halvenstedt.net</p>
  </div>
</body>
</html>
```